Gulf Book About Father - need cover design named - الوهج

The book talks about the good father who teaches his sons high principles and values, to be successful people in their lives.

Book size - 15 cm high
21 cm width
Data on the cover:
Name of the Book: الوهج
Author: دكتور/ وضاح بن ناصر القرملي- Just write the name without the word writer
1440-2018
Logo of the Publishing House

Target Market(s)

Book submitted to children - Families - Schools - Public libraries

Requirements
Must have
• Design must include one or all of these options:
• The first option: a picture that has a meaning for a father who has values and principles with the son or children, expresses the contradiction - education, etc. -
• The background is to express the tender love or taken from the Emirates flag
• The second option: abstract art - with a background taken from the colors of the flag of the Emirates - or colors about love and tenderness
Should not have
• direct image

```html
<!DOCTYPE html>
<html lang="ar" dir="rtl">
<head>
<meta charset="utf-8">
<title>الوهج — غلاف الكتاب</title>
<link rel="stylesheet" href="https://fonts.googleapis.com/css2?family=Baloo+Bhaijaan+2:wght@800&family=Cairo:wght@500;600&display=swap">
<style>
  :root {
    --page-bg: #ecebe6;
    --cover-purple: #4f3192;
    --cover-purple-deep: #3e2580;
    --cover-purple-light: #7a46a8;
    --band: rgba(170, 90, 190, 0.35);
    --ring: #6a2fa0;
    --sky-top: #fff3a6;
    --sky-mid: #ffd27a;
    --ground: #e8285a;
    --title-yellow: #ffe23a;
    --title-glow: #ff4fd0;
    --text-light: #fff3c4;
    --logo-bg: #f4efe6;
    --logo-ink: #6b3b1e;
  }
  html, body {
    margin: 0;
    width: 1200px;
    height: 800px;
    overflow: hidden;
    background: var(--page-bg);
  }
  .book-cover {
    position: absolute;
    left: 75px;
    top: 25px;
    width: 1050px;
    height: 750px;
    overflow: hidden;
    background: radial-gradient(ellipse at 50% 45%, var(--cover-purple) 0%, var(--cover-purple-deep) 100%);
    font-family: "Cairo", sans-serif;
  }
  .cover-band {
    position: absolute;
    left: 0;
    width: 100%;
    background: linear-gradient(90deg, var(--cover-purple-light), var(--band) 50%, var(--cover-purple-light));
    opacity: 0.55;
  }
  .cover-band--top { top: 42px; height: 58px; }
  .cover-band--bottom { top: 610px; height: 56px; }
  .cover-photo {
    position: absolute;
    left: 311px;
    top: 85px;
    width: 460px;
    height: 460px;
  }
  .book-title {
    position: absolute;
    left: 0;
    width: 1082px;
    top: 400px;
    margin: 0;
    text-align: center;
    font-family: "Baloo Bhaijaan 2", sans-serif;
    font-weight: 800;
    font-size: 150px;
    line-height: 1;
    color: var(--title-yellow);
    -webkit-text-stroke: 3px #c0208e;
    paint-order: stroke fill;
    text-shadow: 0 0 18px var(--title-glow), 0 0 36px rgba(255, 79, 208, 0.6);
  }
  .book-author {
    position: absolute;
    left: 0;
    width: 1082px;
    top: 606px;
    margin: 0;
    text-align: center;
    color: var(--text-light);
    font-weight: 600;
    font-size: 27px;
    line-height: 1.35;
  }
  .book-date {
    position: absolute;
    left: 0;
    width: 1082px;
    top: 680px;
    margin: 0;
    text-align: center;
    color: var(--text-light);
    font-weight: 500;
    font-size: 26px;
    letter-spacing: 2px;
  }
  .publisher-mark {
    position: absolute;
    left: 950px;
    top: 610px;
    width: 58px;
    height: 62px;
    background: var(--logo-bg);
    display: flex;
    align-items: center;
    justify-content: center;
    text-align: center;
    color: var(--logo-ink);
    font-weight: 600;
    font-size: 12px;
    line-height: 1.2;
  }
</style>
</head>
<body>
  <main class="book-cover">
    <div class="cover-band cover-band--top"></div>
    <div class="cover-band cover-band--bottom"></div>

    <svg class="cover-photo" viewBox="0 0 460 460" role="img" aria-label="صورة أب يمسك بيد ابنه يسيران في الصحراء بألوان صفراء ووردية">
      <defs>
        <linearGradient id="photo-tone" x1="0" y1="0" x2="0" y2="1">
          <stop offset="0" stop-color="var(--sky-top)"/>
          <stop offset="0.55" stop-color="var(--sky-mid)"/>
          <stop offset="0.78" stop-color="#f79ab8"/>
          <stop offset="1" stop-color="var(--ground)"/>
        </linearGradient>
      </defs>
      <circle cx="230" cy="230" r="228" fill="var(--ring)"/>
      <circle cx="230" cy="230" r="216" fill="url(#photo-tone)"/>
    </svg>

    <h1 class="book-title">الوهج</h1>
    <p class="book-author">دكتور/ وضاح<br>بن ناصر القرملي</p>
    <p class="book-date">١٤٤٠-٢٠١٨</p>

    <div class="publisher-mark">دار<br>الضياء</div>
  </main>
</body>
</html>
```